Corporate Cover & Profile Images - YouTube, Google+, Facebook, Instagram, Twitter, Linkedin, Pint...

I need corporate social media cover & profile images created for YouTube, Google+, Facebook, Instagram, Twitter, Linkedin, and Pintrest. Our logo, an image of our doctors, and fonts are attached. Website URL is corvalemedicalgroup.com. Design must match our overall branding and color scheme. I also need our phone number of 844-555-0172 prominently displayed in the cover images. If you want to incorporate results images they can be found here: https://corvalemedicalgroup.com/results/hair-transplant-before-and-after/ If stock images are used please provide the URL so I can purchase the proper usage license. Must deliver original photoshop PSD files and final images sized correctly for each social account.

```html
<!DOCTYPE html>
<html lang="en">
<head>
<meta charset="utf-8">
<title>Corvale Medical Group – Social Cover Set</title>
<link rel="stylesheet" href="https://fonts.googleapis.com/css2?family=Montserrat:wght@400;500;800&family=Arimo:wght@400&display=swap">
<style>
  :root {
    --board-light: #f2f2f2;
    --board-dark: #d2d2d2;
    --teal: #1f7d72;
    --teal-deep: #17685f;
    --teal-light: #2e9a86;
    --navy: #1f2a5c;
    --navy-deep: #151d44;
    --ink: #3b3a3a;
    --white: #ffffff;
    --label: #1b1b1b;
  }
  * { margin: 0; padding: 0; box-sizing: border-box; }
  html, body { width: 1200px; height: 1200px; overflow: hidden; }
  body {
    background: radial-gradient(ellipse at 50% 10%, var(--board-light) 0%, #e2e2e2 55%, var(--board-dark) 100%);
    position: relative;
    font-family: "Montserrat", sans-serif;
  }
  .cover {
    position: absolute;
    background: var(--white);
    overflow: hidden;
    container-type: inline-size;
    box-shadow: 0 4px 10px rgba(0,0,0,.35);
  }
  .cover .wave { position: absolute; inset: 0; width: 100%; height: 100%; }
  .wave .band { fill: url(#bandGrad); }
  .wave .line { fill: none; stroke: var(--teal-light); stroke-width: .35; }
  .team-photo {
    position: absolute;
    left: 0; bottom: 0;
    width: 57%; height: 78%;
    background: linear-gradient(180deg, #d9c7b4 0%, #c9a993 22%, var(--navy) 42%, var(--navy-deep) 100%);
    border-radius: 40% 40% 0 0 / 18% 18% 0 0;
  }
  .brand {
    position: absolute;
    right: 1.8%; top: 14%;
    text-align: center;
    color: var(--ink);
    font-weight: 500;
    line-height: 1.1;
  }
  .brand-name { font-size: 3.9cqw; letter-spacing: -.02em; white-space: nowrap; }
  .brand-tag { font-size: 1.85cqw; letter-spacing: .01em; }
  .contact {
    position: absolute;
    right: 2.5%; top: 66%;
    color: var(--white);
    line-height: 1.05;
  }
  .phone { font-size: 6.2cqw; font-weight: 800; letter-spacing: .01em; white-space: nowrap; }
  .url { font-size: 3.4cqw; font-weight: 400; padding-left: .2cqw; }

  .cover--youtube   { left: 313px; top: 30px;  width: 577px; height: 315px; }
  .cover--facebook  { left: 466px; top: 386px; width: 270px; height: 141px; }
  .cover--googleplus{ left: 479px; top: 567px; width: 243px; height: 137px; }
  .cover--instagram { left: 508px; top: 734px; width: 186px; height: 70px; }
  .cover--linkedin  { left: 466px; top: 838px; width: 270px; height: 90px; }
  .cover--pinterest { left: 511px; top: 970px; width: 180px; height: 180px; }

  .cover--facebook .team-photo, .cover--googleplus .team-photo { width: 58%; height: 72%; }
  .cover--facebook .brand { top: 10%; }
  .cover--googleplus .brand { top: 10%; }
  .cover--googleplus .brand-name { font-size: 3.6cqw; }
  .cover--instagram .team-photo, .cover--linkedin .team-photo { width: 47%; height: 78%; }
  .cover--instagram .brand, .cover--linkedin .brand { top: 9%; }
  .cover--instagram .brand-name, .cover--linkedin .brand-name { font-size: 3.2cqw; }
  .cover--instagram .brand-tag, .cover--linkedin .brand-tag { font-size: 1.5cqw; }
  .cover--instagram .contact, .cover--linkedin .contact { top: 62%; }
  .cover--instagram .phone, .cover--linkedin .phone { font-size: 5.6cqw; }
  .cover--instagram .url, .cover--linkedin .url { font-size: 3.3cqw; }

  .cover--pinterest .brand { left: 0; right: 0; top: 8%; }
  .cover--pinterest .brand-name { font-size: 5.6cqw; }
  .cover--pinterest .brand-tag { font-size: 2.7cqw; }
  .cover--pinterest .contact { left: 0; right: 0; top: 28%; text-align: center; color: var(--teal); }
  .cover--pinterest .phone { font-size: 9.6cqw; }
  .cover--pinterest .url { font-size: 5.6cqw; color: var(--ink); }
  .cover--pinterest .team-photo { left: 5%; width: 92%; height: 38%; border-radius: 30% 30% 0 0 / 30% 30% 0 0; }

  .cover-label {
    position: absolute;
    left: 0; width: 1200px;
    text-align: center;
    font-family: "Arimo", sans-serif;
    color: var(--label);
  }
</style>
</head>
<body>
  <svg width="0" height="0" style="position:absolute">
    <defs>
      <linearGradient id="bandGrad" x1="0" y1="0" x2="1" y2="1">
        <stop offset="0" stop-color="#1a6f6a"/>
        <stop offset=".5" stop-color="#1f7d72"/>
        <stop offset="1" stop-color="#2d9a80"/>
      </linearGradient>
    </defs>
  </svg>

  <!-- YouTube -->
  <div class="cover cover--youtube">
    <svg class="wave" viewBox="0 0 100 100" preserveAspectRatio="none" aria-hidden="true">
      <path class="band" d="M0,55 C30,62 55,36 78,39 C90,41 96,47 100,50 L100,100 L0,100Z"/>
      <path class="line" d="M48,52 C62,38 80,28 100,42"/>
    </svg>
    <div class="team-photo" role="img" aria-label="Photo of the four-member medical team in navy scrubs with arms crossed"></div>
    <div class="brand"><div class="brand-name">CORVALE MEDICAL GROUP</div><div class="brand-tag">HAIR RESTORATION CLINIC</div></div>
    <div class="contact"><div class="phone">844-555-0172</div><div class="url">corvalemedicalgroup.com</div></div>
  </div>
  <div class="cover-label" style="top:352px;font-size:20px">Youtube Cover</div>

  <!-- Facebook -->
  <div class="cover cover--facebook">
    <svg class="wave" viewBox="0 0 100 100" preserveAspectRatio="none" aria-hidden="true">
      <path class="band" d="M0,58 C30,64 52,40 76,44 C88,46 96,50 100,53 L100,100 L0,100Z"/>
      <path class="line" d="M50,56 C63,42 80,32 100,46"/>
    </svg>
    <div class="team-photo" role="img" aria-label="Photo of the four-member medical team in navy scrubs"></div>
    <div class="brand"><div class="brand-name">CORVALE MEDICAL GROUP</div><div class="brand-tag">HAIR RESTORATION CLINIC</div></div>
    <div class="contact"><div class="phone">844-555-0172</div><div class="url">corvalemedicalgroup.com</div></div>
  </div>
  <div class="cover-label" style="top:533px;font-size:16px">Facebook Cover</div>

  <!-- Google+ -->
  <div class="cover cover--googleplus">
    <svg class="wave" viewBox="0 0 100 100" preserveAspectRatio="none" aria-hidden="true">
      <path class="band" d="M0,60 C30,66 52,42 76,46 C88,48 96,52 100,55 L100,100 L0,100Z"/>
      <path class="line" d="M50,58 C63,44 80,34 100,48"/>
    </svg>
    <div class="team-photo" role="img" aria-label="Photo of the four-member medical team in navy scrubs"></div>
    <div class="brand"><div class="brand-name">CORVALE MEDICAL GROUP</div><div class="brand-tag">HAIR RESTORATION CLINIC</div></div>
    <div class="contact"><div class="phone">844-555-0172</div><div class="url">corvalemedicalgroup.com</div></div>
  </div>
  <div class="cover-label" style="top:713px;font-size:13px">Google+ Cover</div>

  <!-- Instagram -->
  <div class="cover cover--instagram">
    <svg class="wave" viewBox="0 0 100 100" preserveAspectRatio="none" aria-hidden="true">
      <path class="band" d="M0,62 C30,66 50,40 72,44 C86,46 95,50 100,53 L100,100 L0,100Z"/>
      <path class="line" d="M44,56 C60,40 80,30 100,44"/>
    </svg>
    <div class="team-photo" role="img" aria-label="Photo of the four-member medical team in navy scrubs"></div>
    <div class="brand"><div class="brand-name">CORVALE MEDICAL GROUP</div><div class="brand-tag">HAIR RESTORATION CLINIC</div></div>
    <div class="contact"><div class="phone">844-555-0172</div><div class="url">corvalemedicalgroup.com</div></div>
  </div>
  <div class="cover-label" style="top:814px;font-size:10px">Instagram Cover</div>

  <!-- LinkedIn -->
  <div class="cover cover--linkedin">
    <svg class="wave" viewBox="0 0 100 100" preserveAspectRatio="none" aria-hidden="true">
      <path class="band" d="M0,64 C30,68 50,42 72,46 C86,48 95,52 100,55 L100,100 L0,100Z"/>
      <path class="line" d="M44,58 C60,42 80,32 100,46"/>
    </svg>
    <div class="team-photo" role="img" aria-label="Photo of the four-member medical team in navy scrubs"></div>
    <div class="brand"><div class="brand-name">CORVALE MEDICAL GROUP</div><div class="brand-tag">HAIR RESTORATION CLINIC</div></div>
    <div class="contact"><div class="phone">844-555-0172</div><div class="url">corvalemedicalgroup.com</div></div>
  </div>
  <div class="cover-label" style="top:931px;font-size:14px">Linkedin Cover</div>

  <!-- Pinterest -->
  <div class="cover cover--pinterest">
    <svg class="wave" viewBox="0 0 100 100" preserveAspectRatio="none" aria-hidden="true">
      <path class="band" d="M0,82 C25,78 45,60 70,58 C85,57 94,60 100,62 L100,100 L0,100Z"/>
      <path class="line" d="M0,78 C30,70 55,52 100,56"/>
    </svg>
    <div class="team-photo" role="img" aria-label="Photo of the four-member medical team in navy scrubs with arms crossed"></div>
    <div class="brand"><div class="brand-name">CORVALE MEDICAL GROUP</div><div class="brand-tag">HAIR RESTORATION CLINIC</div></div>
    <div class="contact"><div class="phone">844-555-0172</div><div class="url">corvalemedicalgroup.com</div></div>
  </div>
  <div class="cover-label" style="top:1159px;font-size:11px">Pinterest Cover</div>
</body>
</html>
```